Business card for acupunctist in Melbourne. Specialises in Fertility, pre and post natal care, pain

I am looking for a business card which is going to catch people eyes. Two sided, one side in a muted colour (keeping it feminine) (pink or yellow???)maybe with a little simple logo or picture, the other side I was thinking white with 3 colours (pink grey and yellow... Had these in mind.
Info on the card
Maren Quillby Acupuncture

Dr Maren Quillby (TCM Acupuncture)
Acupuncture for balancing body and mind.
Verdant Osprey Clinic
14 Corran Lane, Eastwood 3071.
96274158
0438215074
Marentcm@quorvenmail.com

Some other little logo/ designs I have liked are as follows:
http://www.tessrolfeclinic.com/rates-and-insurance/
http://www.corabethwinslow.com/
http://www.zd-needlework.co.uk/

Target Market(s)

professional women, people in pain, active people, people seeking a healthy lifefstyle.

Industry/Entity Type

Business

Font styles to use
Serif
Sans Serif

Colors
eea4c8
fde08a
aaaaaa

Requirements
Must have
• Must be eye catching, but not too loud and busy. Subltle is good. Simple is also good. The logo could be something that represents growth and health and nurturing. Again not too elaborate, very simple.
Thankyou
Should not have
• Electric colours, crazy fonts, Pictures of yin and yang, candles, or bodies.

```html
<!DOCTYPE html>
<html lang="en">
<head>
<meta charset="utf-8">
<title>Dr Maren Quillby – Business Cards</title>
<link rel="stylesheet" href="https://fonts.googleapis.com/css2?family=Cagliostro&display=swap">
<style>
  :root {
    --charcoal: #4a4a4c;
    --mandala-yellow: #e8dc2e;
    --lemon: #f3e64a;
    --soft-pink: #e77fae;
    --magenta: #e2187e;
    --berry: #b3166b;
    --petal-grey: #6e6e70;
    --paper: #ffffff;
  }
  * { margin: 0; padding: 0; box-sizing: border-box; }
  html, body { width: 1200px; height: 2842px; overflow: hidden; background: var(--paper); }
  body { position: relative; font-family: "Cagliostro", sans-serif; }

  .card { position: absolute; left: 0; width: 1200px; overflow: hidden; }
  .card--front-grey { top: 0; height: 670px; background: var(--charcoal); }
  .card--back-grey { top: 670px; height: 767px; background: var(--charcoal); }
  .card--front-pink { top: 1563px; height: 595px; background: var(--magenta); }
  .card--back-white { top: 2158px; height: 684px; background: var(--paper); }

  .txt { position: absolute; white-space: nowrap; line-height: 1; }

  .practitioner { font-size: 52px; }
  .practitioner small { font-size: 22px; vertical-align: 0.5em; margin-left: 8px; }
  .tagline { font-size: 38px; }
  .clinic-line { font-size: 64px; }
  .clinic-title { font-size: 100px; }
  .contact { font-size: 41px; letter-spacing: 0.5px; }
  .contact p { margin-bottom: 10px; }

  .card--front-grey .txt { color: var(--mandala-yellow); }
  .card--back-grey .txt { color: var(--soft-pink); }
  .card--front-pink .txt { color: var(--lemon); }
  .card--back-white .clinic-title { color: var(--magenta); font-size: 116px; left: 0; width: 1200px; text-align: center; }
  .card--back-white .contact { color: var(--berry); }

  .ornament { position: absolute; }
  .ornament--mandala-left {
    left: -330px; top: -10px; width: 660px; height: 690px; border-radius: 50%;
    background: radial-gradient(circle, rgba(232,220,46,0.05) 35%, rgba(232,220,46,0.35) 70%, rgba(232,220,46,0.1) 100%);
  }
  .ornament--mandala-right {
    left: 840px; top: 20px; width: 720px; height: 740px; border-radius: 50%;
    background: radial-gradient(circle, rgba(231,127,174,0.35) 20%, rgba(231,127,174,0.2) 60%, rgba(231,127,174,0.05) 100%);
  }
  .ornament--flowers-yellow-left {
    left: 10px; top: 240px; width: 190px; height: 355px;
    background: linear-gradient(to bottom, rgba(243,230,74,0.55), rgba(243,230,74,0.15));
  }
  .ornament--flowers-yellow-right {
    left: 1004px; top: 380px; width: 164px; height: 215px;
    background: linear-gradient(to bottom, rgba(243,230,74,0.55), rgba(243,230,74,0.15));
  }
  .ornament--flowers-grey-hanging {
    left: 1004px; top: 0; width: 164px; height: 290px;
    background: linear-gradient(to bottom, rgba(110,110,112,0.15), rgba(110,110,112,0.5));
  }
  .ornament--flowers-pink-left {
    left: 16px; top: 337px; width: 190px; height: 347px;
    background: linear-gradient(to bottom, rgba(226,24,126,0.45), rgba(226,24,126,0.12));
  }
</style>
</head>
<body>

  <section class="card card--front-grey">
    <div class="ornament ornament--mandala-left" role="img" aria-label="Yellow line-drawn mandala ornament at the left edge"></div>
    <p class="txt practitioner" style="left:433px; top:242px;">Dr Maren Quillby<small>(TCM Acupuncture)</small></p>
    <p class="txt tagline" style="left:433px; top:300px;">Acupuncture for balancing body and mind.</p>
    <p class="txt clinic-line" style="left:433px; top:352px;">Verdant Osprey Clinic</p>
  </section>

  <section class="card card--back-grey">
    <div class="ornament ornament--mandala-right" role="img" aria-label="Pink line-drawn mandala ornament at the right edge"></div>
    <h1 class="txt clinic-title" style="left:95px; top:134px;">Verdant Osprey</h1>
    <h1 class="txt clinic-title" style="left:95px; top:245px;">Clinic</h1>
    <address class="txt contact" style="left:25px; top:472px; font-style:normal;">
      <p>14 Corran Lane, Eastwood 3071.</p>
      <p>96274158</p>
      <p>0438215074</p>
      <p>Marentcm@quorvenmail.com</p>
    </address>
  </section>

  <section class="card card--front-pink">
    <div class="ornament ornament--flowers-yellow-left" role="img" aria-label="Yellow daisies on tall thin stems"></div>
    <div class="ornament ornament--flowers-yellow-right" role="img" aria-label="Yellow daisies on tall thin stems"></div>
    <p class="txt practitioner" style="left:237px; top:70px;">Dr Maren Quillby<small>(TCM Acupuncture)</small></p>
    <p class="txt tagline" style="left:237px; top:134px;">Acupuncture for balancing body and mind.</p>
    <p class="txt clinic-line" style="left:237px; top:230px;">Verdant Osprey Clinic</p>
  </section>

  <section class="card card--back-white">
    <div class="ornament ornament--flowers-grey-hanging" role="img" aria-label="Grey daisies hanging from stems"></div>
    <div class="ornament ornament--flowers-pink-left" role="img" aria-label="Pink daisies on tall thin stems"></div>
    <h1 class="txt clinic-title" style="top:100px;">Verdant Osprey</h1>
    <h1 class="txt clinic-title" style="top:243px;">Clinic</h1>
    <address class="txt contact" style="left:237px; top:418px; font-style:normal;">
      <p>14 Corran Lane, Eastwood 3071.</p>
      <p>96274158</p>
      <p>0438215074</p>
      <p>Marentcm@quorvenmail.com</p>
    </address>
  </section>

</body>
</html>
```